Business card design reauest

2 sided. White on both sides

Gordon Mabry

Ho Chi Minh, Vietnam

Cell Phone / Whatsapp/ Wechat/Zalo
1-555-382-7194
Gmabry@kwpartsworks.vn
Www.kwpartsworks.vn
Www.kwpartsworks.com

Industry/Entity Type

Sofa and furniture and kitchen

Contact Information for Business Card

2 sided. White on both sides Gordon Mabry Ho Chi Minh, Vietnam Cell Phone / Whatsapp/ Wechat/Zalo 1-555-382-7194 Gmabry@kwpartsworks.vn Www.kwpartsworks.vn Www.kwpartsworks.com

```html
<!DOCTYPE html>
<html lang="en">
<head>
<meta charset="utf-8">
<title>KW Parts Works — Business Card</title>
<link rel="stylesheet" href="https://fonts.googleapis.com/css2?family=Montserrat:wght@400;600;700&display=swap">
<style>
  :root {
    --backdrop: #3b3b3b;
    --card-white: #ffffff;
    --brand-green: #169c4a;
    --ink: #222222;
    --shadow: rgba(0, 0, 0, 0.55);
  }
  * { margin: 0; padding: 0; box-sizing: border-box; }
  html, body {
    width: 1200px;
    height: 1059px;
    overflow: hidden;
    background: var(--backdrop);
    font-family: "Montserrat", sans-serif;
  }
  .canvas { position: relative; width: 1200px; height: 1059px; }

  .card {
    position: absolute;
    overflow: hidden;
    box-shadow: 0 14px 22px var(--shadow);
  }
  .card--front {
    left: 256px; top: 100px;
    width: 688px; height: 391px;
    background: var(--card-white);
    color: var(--ink);
  }
  .card--back {
    left: 253px; top: 537px;
    width: 694px; height: 394px;
    background: var(--brand-green);
    display: flex; align-items: center; justify-content: center;
  }

  .brand-name {
    font-weight: 600;
    letter-spacing: 0.04em;
    text-align: center;
    line-height: 1;
    white-space: nowrap;
  }
  .card--front .brand-name {
    position: absolute;
    right: 29px; top: 150px;
    transform: translateY(-50%);
    font-size: 28px;
    color: var(--brand-green);
  }
  .card--back .brand-name {
    font-size: 42px;
    color: var(--card-white);
  }

  .name-tab {
    position: absolute;
    left: 0; top: 194px;
    width: 19px; height: 45px;
    background: var(--brand-green);
    border-radius: 0 5px 5px 0;
  }
  .holder-name {
    position: absolute;
    left: 32px; top: 190px;
    font-size: 28px; font-weight: 700;
    color: var(--brand-green);
    line-height: 1.1;
    white-space: nowrap;
  }
  .holder-role {
    position: absolute;
    left: 32px; top: 225px;
    font-size: 15px; font-weight: 400;
  }
  .divider {
    position: absolute;
    left: 32px; top: 258px;
    width: 627px; height: 2px;
    background: var(--brand-green);
  }

  .contact-list {
    position: absolute;
    left: 32px; top: 276px;
    list-style: none;
  }
  .contact-list li {
    display: flex; align-items: center;
    height: 23.3px;
    font-size: 16px;
    letter-spacing: 0.02em;
    white-space: nowrap;
  }
  .contact-list svg {
    width: 13px; height: 13px;
    margin-right: 8px;
    fill: var(--brand-green);
    flex: none;
  }
  .location {
    position: absolute;
    right: 29px; top: 346px;
    display: flex; align-items: center;
    font-size: 16px;
    letter-spacing: 0.02em;
    white-space: nowrap;
  }
  .location svg {
    width: 12px; height: 17px;
    margin-left: 9px;
    fill: var(--brand-green);
  }
</style>
</head>
<body>
<main class="canvas">

  <section class="card card--front" aria-label="Business card front">
    <p class="brand-name">KW PARTS WORKS</p>

    <span class="name-tab"></span>
    <h1 class="holder-name">Gordon Mabry</h1>
    <p class="holder-role">Manager</p>
    <span class="divider"></span>

    <ul class="contact-list">
      <li>
        <svg viewBox="0 0 16 16" aria-hidden="true"><path d="M3.6 1.2l2.3 2.6c.4.5.4 1.1 0 1.6L4.8 6.6c.9 2 2.5 3.6 4.5 4.5l1.2-1.1c.5-.4 1.1-.4 1.6 0l2.6 2.3c.5.4.5 1.1 0 1.6l-1.3 1.3C11.7 16.9 0 9 .8 2.6L2 1.2c.5-.5 1.2-.5 1.6 0z"/></svg>
        1-555-382-7194
      </li>
      <li>
        <svg viewBox="0 0 16 16" aria-hidden="true"><path d="M0 3h16v1.5L8 9 0 4.5z"/><path d="M0 6.3l8 4.5 8-4.5V13H0z"/></svg>
        gmabry@kwpartsworks.vn
      </li>
      <li>
        <svg viewBox="0 0 16 16" aria-hidden="true"><path d="M8 0a8 8 0 100 16A8 8 0 008 0zm0 1.5c.9 0 1.9 1.6 2.3 4H5.7C6.1 3.1 7.1 1.5 8 1.5zM5.5 7h5a14 14 0 010 2h-5a14 14 0 010-2zm-1.5 0a16 16 0 000 2H1.6a6.5 6.5 0 010-2zm8 0h2.4a6.5 6.5 0 010 2H12a16 16 0 000-2zM4.2 5.5H2.2a6.5 6.5 0 013.4-3.5c-.6 1-1.1 2.1-1.4 3.5zm7.6 0c-.3-1.4-.8-2.5-1.4-3.5a6.5 6.5 0 013.4 3.5zM2.2 10.5h2c.3 1.4.8 2.5 1.4 3.5a6.5 6.5 0 01-3.4-3.5zm3.5 0h4.6c-.4 2.4-1.4 4-2.3 4s-1.9-1.6-2.3-4zm6.1 0h2a6.5 6.5 0 01-3.4 3.5c.6-1 1.1-2.1 1.4-3.5z"/></svg>
        www.kwpartsworks.vn
      </li>
      <li>
        <svg viewBox="0 0 16 16" aria-hidden="true"><path d="M8 0a8 8 0 100 16A8 8 0 008 0zm0 1.5c.9 0 1.9 1.6 2.3 4H5.7C6.1 3.1 7.1 1.5 8 1.5zM5.5 7h5a14 14 0 010 2h-5a14 14 0 010-2zm-1.5 0a16 16 0 000 2H1.6a6.5 6.5 0 010-2zm8 0h2.4a6.5 6.5 0 010 2H12a16 16 0 000-2zM4.2 5.5H2.2a6.5 6.5 0 013.4-3.5c-.6 1-1.1 2.1-1.4 3.5zm7.6 0c-.3-1.4-.8-2.5-1.4-3.5a6.5 6.5 0 013.4 3.5zM2.2 10.5h2c.3 1.4.8 2.5 1.4 3.5a6.5 6.5 0 01-3.4-3.5zm3.5 0h4.6c-.4 2.4-1.4 4-2.3 4s-1.9-1.6-2.3-4zm6.1 0h2a6.5 6.5 0 01-3.4 3.5c.6-1 1.1-2.1 1.4-3.5z"/></svg>
        www.kwpartsworks.com
      </li>
    </ul>

    <p class="location">
      Ho Chi Minh, Vietnam
      <svg viewBox="0 0 12 17" aria-hidden="true"><path d="M6 0a6 6 0 00-6 6c0 4.5 6 11 6 11s6-6.5 6-11a6 6 0 00-6-6zm0 8.6A2.6 2.6 0 116 3.4a2.6 2.6 0 010 5.2z"/></svg>
    </p>
  </section>

  <section class="card card--back" aria-label="Business card back">
    <p class="brand-name">KW PARTS WORKS</p>
  </section>

</main>
</body>
</html>
```